High-end Packaging Design For Permanent Holiday Lights

We need a design for our product box for our company HaloSpan which sells permanent Christmas lights.
Box dimensions: 12.69 X 12.69 X 2.06
The box contains a starter kit and lights for customers who want to install their own permanent holiday lights. We want to see classy minimalistic designs the incorporate our logo and brand guidelines.

More white space and use of our logo.

Do not use random imagines of Christmas lights or weird shapes for the design.

This should mimic the style of an orvane zumrik packaging or high end laptop etc.

Target Market(s)

35+ men and women who love the holidays

Industry/Entity Type

Holiday lights

Font styles to use
Other font styles liked:
• Gotham

Requirements
Must have
• Must have our logo, must be classy/high end, must give multiple color options.
Nice to have
• Possible raised foil logo, or different ideas for our logo elements, play around with layouts for the box dimensions.
Should not have
• shouldn't contain any Christmas design elements as our product is used year round,

```html
<!DOCTYPE html>
<html lang="en">
<head>
<meta charset="utf-8">
<title>HaloSpan – Permanent Holiday Lights Starter Kit</title>
<link rel="stylesheet" href="https://fonts.googleapis.com/css2?family=Jost:wght@300;400;600&display=swap">
<style>
  :root {
    --page-bg: #ffffff;
    --band-white: #ececec;
    --panel-black: #2a2a2a;
    --ink-dark: #222222;
    --ink-light: #e6e6e6;
    --rule: #9a9a9a;
  }
  * { margin: 0; padding: 0; box-sizing: border-box; }
  html, body {
    width: 1200px;
    height: 1029px;
    overflow: hidden;
    background: var(--page-bg);
  }
  .box-face {
    position: absolute;
    left: 290px;
    top: 204px;
    width: 620px;
    height: 620px;
    display: flex;
  }
  .brand-band {
    width: 205px;
    height: 100%;
    background: var(--band-white);
    display: flex;
    justify-content: center;
  }
  .brand-name {
    margin-top: 96px;
    font-family: 'Jost', sans-serif;
    font-weight: 400;
    font-size: 17px;
    letter-spacing: 4px;
    text-transform: uppercase;
    color: var(--ink-dark);
  }
  .product-panel {
    position: relative;
    flex: 1;
    height: 100%;
    background: var(--panel-black);
  }
  .colour-disc {
    position: absolute;
    left: 50%;
    top: 258px;
    width: 305px;
    height: 305px;
    transform: translate(-50%, -50%);
    border-radius: 50%;
    background:
      radial-gradient(circle, rgba(190,170,170,0.55) 0%, rgba(190,170,170,0.15) 35%, rgba(190,170,170,0) 65%),
      conic-gradient(from 0deg,
        #2f7fe6 0deg,
        #4a5ae8 55deg,
        #8a3fe0 95deg,
        #b03ccf 125deg,
        #e8389a 170deg,
        #f0607a 205deg,
        #f0a045 235deg,
        #e6e22c 265deg,
        #9ade3a 295deg,
        #3ccf6a 320deg,
        #2aa8d8 345deg,
        #2f7fe6 360deg);
  }
  .product-title {
    position: absolute;
    left: 30px;
    top: 534px;
    padding-left: 7px;
    border-left: 1px solid var(--rule);
    color: var(--ink-light);
    font-family: 'Jost', sans-serif;
  }
  .product-line {
    font-weight: 300;
    font-size: 17px;
    letter-spacing: 2.6px;
    text-transform: uppercase;
    line-height: 22px;
  }
  .product-kit {
    font-weight: 600;
    font-size: 15px;
    letter-spacing: 2px;
    line-height: 22px;
  }
</style>
</head>
<body>
  <main class="box-face">
    <section class="brand-band">
      <p class="brand-name">HaloSpan</p>
    </section>
    <section class="product-panel">
      <div class="colour-disc" role="img" aria-label="Full-spectrum colour wheel showing the range of light colours"></div>
      <div class="product-title">
        <p class="product-line">Permanent Holiday Lights</p>
        <p class="product-kit">starter kit</p>
      </div>
    </section>
  </main>
</body>
</html>
```